Design business cards for Ironvale Barbers (Opening March so won't need finalised till January2018

Ironvale Barbers is the new age barbers and skincare for all men. Creating tailor made haircuts & customised skincare solutions for the perfect healthy manly look. The Barbers will have a industrial, rustic, worldly feel about it. Rustic red brick wall with old wine barrels as the work stations with the old fashion barber chairs. Concrete floor and a bit corrugated iron around.
Target Market(s)
Professional males who like a great haircut, wet shave and may consider a facial if in the right environment. Total pampering experience in a boys environment.
Industry/Entity Type
Barber
Contact Information for Business Card
Front- Logo - address is 42 Kowhai Rd Taupo
Ph - (07) 548 9163
www.ironvalebarbers.com
email - hello@ironvale.co.nz
Back of card
Mens Haircare - Wet Shaving - Facials - Skin Prescriptions
We are doing a loyalty program - 6 squares numbered then 7th free
Colors
Designer to choose colors to be used in the design.
Requirements
Must have
- Clean simple easy to read.
Nice to have
- Our current colours are white font on black background but thinking we need to introduce another colour. Maybe white logo on a copper, bronze or rusty background. Or even a rustic red brick wall with white writing. Want it clean simple to read. Maybe a burgundy?
Should not have
- no images like heads, scissors, razors please

```html
<!DOCTYPE html>
<html lang="en">
<head>
<meta charset="utf-8">
<title>Ironvale Barbers – Business Cards</title>
<link href="https://fonts.googleapis.com/css2?family=Stint+Ultra+Condensed&display=swap" rel="stylesheet">
<style>
  :root {
    --backdrop: #1b1b1b;
    --brick-dark: #6c5a4a;
    --brick-mid: #8a7560;
    --brick-warm: #947058;
    --burgundy: #8b181b;
    --white: #ffffff;
    --ink-red: #8b181b;
  }
  * { margin: 0; padding: 0; box-sizing: border-box; }
  html, body {
    width: 1200px;
    height: 897px;
    overflow: hidden;
    background: var(--backdrop);
  }
  body {
    position: relative;
    font-family: "Stint Ultra Condensed", "Times New Roman", serif;
    color: var(--white);
    text-transform: uppercase;
  }
  .card {
    position: absolute;
    left: 304px;
    width: 594px;
    height: 338px;
    border-radius: 19px;
    overflow: hidden;
  }
  .card-front { top: 92px; }
  .card-back { top: 470px; background: var(--burgundy); }

  .brick-wall {
    position: absolute;
    inset: 0;
    background:
      radial-gradient(ellipse at 30% 40%, rgba(150,110,85,0.45), transparent 60%),
      radial-gradient(ellipse at 75% 70%, rgba(120,125,95,0.35), transparent 60%),
      linear-gradient(160deg, var(--brick-mid), var(--brick-dark) 55%, var(--brick-warm));
  }

  .brand-name {
    position: absolute;
    top: 78px;
    left: 0;
    right: 0;
    text-align: center;
    font-size: 62px;
    line-height: 1;
    letter-spacing: 1px;
  }

  .contact-line {
    position: absolute;
    left: 0;
    right: 0;
    text-align: center;
    white-space: nowrap;
  }
  .contact-primary { top: 211px; font-size: 27px; letter-spacing: 0.5px; }
  .contact-secondary { top: 248px; font-size: 20px; letter-spacing: 0.3px; }
  .divider { margin: 0 8px; }

  .services {
    position: absolute;
    top: 128px;
    left: 0;
    right: 0;
    text-align: center;
    font-size: 29px;
    line-height: 36px;
    letter-spacing: 1px;
  }

  .appointment-strip {
    position: absolute;
    left: 37px;
    top: 272px;
    width: 520px;
    height: 41px;
    background: var(--white);
    color: var(--ink-red);
    font-size: 24px;
    line-height: 41px;
    padding-left: 10px;
    white-space: nowrap;
    letter-spacing: 0.5px;
  }
</style>
</head>
<body>
  <section class="card card-front">
    <div class="brick-wall" role="img" aria-label="Rustic red brick wall texture"></div>
    <div class="brand-name">Ironvale Barbers</div>
    <p class="contact-line contact-primary">Cell: (07) 548 9163<span class="divider">|</span>42 Kowhai Rd Taupo</p>
    <p class="contact-line contact-secondary">hello@ironvale.co.nz<span class="divider">|</span>www.ironvalebarbers.com</p>
  </section>

  <section class="card card-back">
    <p class="services">Mens Haircare - Wet Shaving<br>Facials - Skin Prescriptions</p>
    <div class="appointment-strip">Date: _ _ / _ _ / _ _ _ _ _Time: _ _ _ _ _ _ _ _ _</div>
  </section>
</body>
</html>
```